Core Values Poster for Healthcare company

Trying to Create a core values poster for my company. Healthcare Company - We have Neurosurgery, Pain Management, Physical Therapy, Occupational Therapy, Rehab, Imaging, and psychology so far and we are growing fast.

Core Values would Include - (Execution), (Loyalty), (Innovation), (Synergy), (Growth-Oriented), (Ethics & Integrity), (Love), and (Energy)

Please incorporate the Company Logo which is on the website and I have included it in my uploads. As long as the logo stays blue it does not need a gradient effect.

I like the posters made for this contest : https://pinlarkstudio.com.au/flyer-work/briefs/build-team-ideals-flyer-580316

This picture should be memorable so people know our Core Values

Target Market(s)

Staff in the company

Colors

Designer to choose colors to be used in the design.

Requirements
Must have
• Logo
Nice to have
• Pictures for each core value

```html
<!DOCTYPE html>
<html lang="en">
<head>
<meta charset="utf-8">
<title>Vantora Core Values</title>
<link href="https://fonts.googleapis.com/css2?family=Questrial&display=swap" rel="stylesheet">
<style>
  :root {
    --bg-light: #f4f5f6;
    --bg-dark: #d9dbdd;
    --band: #2aaec5;
    --title: #1f5566;
    --brand: #1e8fc8;
    --execution: #17596b;
    --loyalty: #2bb0c7;
    --innovation: #ec9a2e;
    --synergy: #7bb843;
    --growth: #e9722f;
    --ethics: #a9aaab;
    --love: #2bb0c7;
    --energy: #f0a02c;
    --side-blue: #aed7df;
    --side-tan: #e3c8a3;
    --frame: #eeeff0;
  }
  html, body { margin: 0; padding: 0; overflow: hidden; }
  body { width: 1200px; height: 848px; }
  .poster {
    display: block;
    width: 1200px;
    height: 848px;
    font-family: "Questrial", sans-serif;
  }
  .value-label {
    fill: #fff;
    font-size: 25px;
    letter-spacing: 1px;
    text-anchor: middle;
    dominant-baseline: middle;
  }
  .icon { fill: none; stroke: #fff; stroke-width: 6; stroke-linecap: round; stroke-linejoin: round; }
  .icon-fill { fill: #fff; }
  .piece { stroke: #fff; stroke-width: 10; stroke-linejoin: round; }
</style>
</head>
<body>
<svg class="poster" viewBox="0 0 1500 1060" xmlns="http://www.w3.org/2000/svg">
  <defs>
    <linearGradient id="backdrop" x1="0" y1="0" x2="1" y2="1">
      <stop offset="0" stop-color="var(--bg-light)"/>
      <stop offset="1" stop-color="var(--bg-dark)"/>
    </linearGradient>
    <filter id="lift" x="-20%" y="-20%" width="140%" height="140%">
      <feDropShadow dx="6" dy="8" stdDeviation="7" flood-color="#000" flood-opacity="0.25"/>
    </filter>
    <polygon id="segment" points="-145,-350 145,-350 83,-200 -83,-200"/>
  </defs>

  <rect width="1500" height="1060" fill="url(#backdrop)"/>

  <!-- Header -->
  <rect x="0" y="72" width="595" height="26" fill="var(--band)"/>
  <rect x="880" y="72" width="620" height="26" fill="var(--band)"/>
  <text x="737" y="97" fill="var(--title)" font-size="38" letter-spacing="1.5" text-anchor="middle">CORE VALUES</text>

  <!-- Side puzzle panels -->
  <g class="side-panel" filter="url(#lift)">
    <path d="M0 215 L210 230 A40 40 0 0 1 280 300 L355 345 L355 640 L290 680 A40 40 0 0 0 230 740 L0 810 Z" fill="var(--frame)"/>
    <path d="M30 250 L330 370 L330 620 L260 655 A60 60 0 0 0 145 705 L30 770 Z" fill="var(--side-blue)"/>
  </g>
  <g class="side-panel" filter="url(#lift)">
    <path d="M1500 205 L1500 830 L1290 800 A40 40 0 0 1 1230 740 L1125 700 L1125 380 L1210 330 A40 40 0 0 0 1280 265 Z" fill="var(--frame)"/>
    <path d="M1460 245 L1460 785 L1150 660 L1150 370 L1215 345 A80 80 0 0 0 1395 270 Z" fill="var(--side-tan)"/>
  </g>

  <!-- Value ring -->
  <g class="value-ring" transform="translate(740 520)" filter="url(#lift)">
    <use href="#segment" class="piece" fill="var(--execution)"/>
    <use href="#segment" class="piece" fill="var(--loyalty)" transform="rotate(45)"/>
    <use href="#segment" class="piece" fill="var(--innovation)" transform="rotate(90)"/>
    <use href="#segment" class="piece" fill="var(--synergy)" transform="rotate(135)"/>
    <use href="#segment" class="piece" fill="var(--growth)" transform="rotate(180)"/>
    <use href="#segment" class="piece" fill="var(--ethics)" transform="rotate(225)"/>
    <use href="#segment" class="piece" fill="var(--love)" transform="rotate(270)"/>
    <use href="#segment" class="piece" fill="var(--energy)" transform="rotate(315)"/>
    <g fill="#e6e7e8">
      <circle cx="-114" cy="-275" r="18" transform="rotate(0)"/>
      <circle cx="-114" cy="-275" r="18" transform="rotate(45)"/>
      <circle cx="-114" cy="-275" r="18" transform="rotate(90)"/>
      <circle cx="-114" cy="-275" r="18" transform="rotate(135)"/>
      <circle cx="-114" cy="-275" r="18" transform="rotate(180)"/>
      <circle cx="-114" cy="-275" r="18" transform="rotate(225)"/>
      <circle cx="-114" cy="-275" r="18" transform="rotate(270)"/>
      <circle cx="-114" cy="-275" r="18" transform="rotate(315)"/>
    </g>
  </g>

  <!-- Labels -->
  <text class="value-label" x="744" y="192">EXECUTION</text>
  <text class="value-label" transform="translate(966 284) rotate(45)">LOYALTY</text>
  <text class="value-label" transform="translate(1066 522) rotate(90)">INNOVATION</text>
  <text class="value-label" transform="translate(958 756) rotate(-45)">SYNERGY</text>
  <text class="value-label" x="726" y="816">GROWTH-</text>
  <text class="value-label" x="726" y="847">ORIENTED</text>
  <text class="value-label" transform="translate(515 730) rotate(45)">ETHICS &amp;</text>
  <text class="value-label" transform="translate(496 746) rotate(45)">INTEGRITY</text>
  <text class="value-label" transform="translate(407 516) rotate(90)">LOVE</text>
  <text class="value-label" transform="translate(508 284) rotate(-45)">ENERGY</text>

  <!-- Icons -->
  <g class="icon" transform="translate(740 250)">
    <rect x="-22" y="-28" width="44" height="58" rx="3"/>
    <rect x="-8" y="-36" width="16" height="10" rx="2"/>
    <path d="M-12 0 L-2 14 L16 -16"/>
  </g>
  <g class="icon" transform="translate(552 326)">
    <circle r="32"/>
    <path class="icon-fill" stroke="none" d="M4 -22 L-12 4 L0 4 L-6 22 L12 -6 L0 -6 Z"/>
  </g>
  <g class="icon" transform="translate(922 328) rotate(-20)">
    <path d="M-38 8 L-10 28 L20 28 L38 8"/>
    <path d="M-38 -8 L-10 -28 L20 -28 L38 -8"/>
    <circle r="11"/>
  </g>
  <g class="icon" transform="translate(1004 515)">
    <path d="M-14 20 A24 24 0 1 1 14 20 L14 30 L-14 30 Z"/>
    <path d="M-10 40 L10 40 M-6 -2 L0 8 L6 -2 M0 8 L0 22"/>
    <path d="M-40 0 L-34 0 M34 0 L40 0 M0 -44 L0 -38 M-28 -30 L-24 -26 M28 -30 L24 -26"/>
  </g>
  <g class="icon" transform="translate(912 708)">
    <path d="M-26 -6 A26 26 0 0 1 10 -26 M26 6 A26 26 0 0 1 -10 26 M-6 26 A26 26 0 0 1 -26 -10"/>
    <circle class="icon-fill" stroke="none" cx="0" cy="-34" r="8"/>
    <circle class="icon-fill" stroke="none" cx="30" cy="18" r="8"/>
    <circle class="icon-fill" stroke="none" cx="-30" cy="18" r="8"/>
  </g>
  <g class="icon-fill" transform="translate(728 768)">
    <rect x="-32" y="10" width="11" height="20"/>
    <rect x="-16" y="0" width="11" height="30"/>
    <rect x="0" y="-10" width="11" height="40"/>
    <rect x="16" y="-22" width="11" height="52"/>
    <path class="icon" d="M-34 0 L-10 -16 L6 -8 L36 -34"/>
    <path d="M26 -40 L42 -40 L42 -24 Z"/>
  </g>
  <g class="icon" transform="translate(562 682) rotate(15)">
    <rect x="-24" y="-22" width="34" height="40" rx="4"/>
    <path d="M10 -6 L28 -6 L28 20 L-24 20"/>
    <path d="M-16 -10 L2 -10 M-16 2 L2 2"/>
  </g>
  <g class="icon" transform="translate(470 516)">
    <path d="M0 26 L-26 0 A15 15 0 0 1 0 -20 A15 15 0 0 1 26 0 Z"/>
  </g>

  <!-- Center brand tile -->
  <g filter="url(#lift)">
    <rect x="620" y="408" width="240" height="240" rx="26" fill="var(--brand)"/>
  </g>
  <text x="740" y="530" fill="#fff" font-size="40" letter-spacing="2" text-anchor="middle" dominant-baseline="middle">VANTORA</text>

  <!-- Footer brand -->
  <rect x="470" y="940" width="85" height="85" rx="4" fill="var(--brand)"/>
  <text x="578" y="1014" fill="var(--brand)" font-size="84" letter-spacing="4">VANTORA</text>
</svg>
</body>
</html>
```